Bramblewick Systems Group - IT Services Company/Managed Services/Consulting Card Design

Our company needs a business card design that will appeal to client companies with 50-1000 employees. We do IT services, administration, management, projects, budgeting and consulting (Like a small Corvatel.com, Plumvary.com or Tundrabox.com). Mainly helping businesses use technology to be more competitive and efficient. We work with IT Infrastructure, switches, routers, firewalls and Cloud, Verlanta/Linux servers, Quellon server virtualization, Datacenter environments, Email systems, Business Systems, Backup, Disaster Recovery, Data Security, NVX, Deskora 12 and Halcyte.) Would like the final design to be professional but stand out to our prospective clients. Our current logo is attached. Color or design could be changed. Overall looking for a great finished product, original ideas are welcome and would pay more for the right one. If you think you have a better logo idea include a general idea if you can. Web design has not been done yet so that is a later possibility too.

Target Market(s)

1st - Mid-sized companies with 100-1000 employees with technology needs
2nd - Smaller companies with 20-99 employees with technology needs
- These companies can be in many different industries. Heathcare, legal, manufacturing, education, non-profit, services

Industry/Entity Type

Information Technology

Contact Information for Business Card

Should include the following info:

Logo or other logo with Company Name

Martin J. Cosgrove

Principal

BramblewickSys.com

mcosgrove@BramblewickSys.com

(866) 7-BRAMBLE x 348

Font styles to use
Other font styles liked:
• designer can decide

Requirements
Must have
• Professional, appealing design, appeal to the target market
Nice to have
• Some sort of additional accent design that would stand out could be nice. I thought of adding a graphic in the top left corner that would look like the corner of the card was becoming more and more pixelated as it got near the corner, with some pixels missing.

```html
<!DOCTYPE html>
<html lang="en">
<head>
<meta charset="utf-8">
<title>Bramblewick Systems Group – Business Card</title>
<link rel="stylesheet" href="https://fonts.googleapis.com/css2?family=Arvo:wght@400;700&display=swap">
<style>
  :root {
    --backdrop: #e9e7e4;
    --card: #ffffff;
    --ink: #231f20;
    --ink-soft: #3a3a3c;
    --blue: #1a6fbf;
    --blue-light: #7fc6e0;
    --orange: #f5a733;
    --orange-deep: #ef7d2f;
    --slate: #3d4556;
    --dark: #231f20;
  }
  * { box-sizing: border-box; margin: 0; padding: 0; }
  html, body {
    width: 1200px; height: 987px; overflow: hidden;
    background: var(--backdrop);
    font-family: "Arvo", Georgia, serif;
    color: var(--ink);
  }
  .card {
    position: absolute; left: 293px; width: 615px; height: 352px;
    background: var(--card); overflow: hidden;
    box-shadow: 0 2px 6px rgba(0,0,0,.18);
  }
  .card--front { top: 129px; }
  .card--back  { top: 505px; }

  .card__art { position: absolute; left: 0; top: 0; }

  .brand {
    position: absolute; display: flex; align-items: center; gap: 12px;
  }
  .brand__mark { width: 18px; height: 18px; background: var(--blue); flex: none; }
  .brand__name {
    font-weight: 700; font-size: 27px; line-height: 1.1;
    color: var(--ink); letter-spacing: .5px;
  }
  .card--front .brand { right: 42px; top: 38px; text-align: right; }
  .card--back .brand { left: 0; right: 0; top: 60px; justify-content: center; }

  .person { position: absolute; right: 42px; top: 172px; text-align: right; }
  .person__name { font-size: 21px; color: var(--ink); }
  .person__role { font-size: 15px; color: var(--ink); margin-top: 2px; }

  .contact {
    position: absolute; right: 22px; top: 264px; list-style: none;
    font-size: 14.5px; color: var(--ink-soft);
  }
  .contact li {
    display: flex; align-items: center; justify-content: flex-end;
    gap: 9px; height: 23px;
  }
  .contact svg { width: 15px; height: 15px; flex: none; }

  .card__base {
    position: absolute; left: 0; right: 0; top: 195px; bottom: 0;
    background: var(--dark);
  }
  .services {
    position: absolute; left: 0; right: 0; top: 252px;
    text-align: center; color: #fff; font-size: 15px; line-height: 23px;
  }
  .services__row { display: flex; justify-content: center; align-items: center; gap: 5px; }
  .services svg { width: 13px; height: 13px; }
</style>
</head>
<body>

<section class="card card--front" aria-label="Business card front">
  <svg class="card__art" width="615" height="352" viewBox="0 0 615 352">
    <defs>
      <linearGradient id="pixelTone" x1="0" y1="0" x2="1" y2="1">
        <stop offset="0" stop-color="#f5a733"/>
        <stop offset=".45" stop-color="#7fc6e0"/>
        <stop offset="1" stop-color="#d8eef6"/>
      </linearGradient>
      <linearGradient id="band" x1="0" y1="0" x2="1" y2="0">
        <stop offset="0" stop-color="#3d4556"/>
        <stop offset=".6" stop-color="#1a6fbf"/>
        <stop offset="1" stop-color="#ffffff"/>
      </linearGradient>
    </defs>
    <polygon points="0,0 258,0 140,190 0,196" fill="url(#pixelTone)" role="img" aria-label="Pixelated corner pattern of small orange, blue and charcoal squares"/>
    <polygon points="0,240 110,240 60,310 0,330" fill="url(#pixelTone)" opacity=".7" role="img" aria-label="Scattered pixel squares below the band"/>
    <polygon points="0,196 615,158 615,240 0,240" fill="url(#band)"/>
  </svg>

  <div class="brand">
    <span class="brand__name">Bramblewick<br>Systems Group</span>
    <span class="brand__mark"></span>
  </div>

  <div class="person">
    <p class="person__name">Martin J. Cosgrove</p>
    <p class="person__role">Principal</p>
  </div>

  <ul class="contact">
    <li>(866) 7-BRAMBLE x 348
      <svg viewBox="0 0 16 16" aria-hidden="true"><path d="M3.5 1.5l2.5 0 1 3.5-1.6 1.2a8 8 0 0 0 4.4 4.4L11 9l3.5 1v2.5c0 1-1 2-2 2A11 11 0 0 1 1.5 3.5c0-1 1-2 2-2z" fill="var(--blue)"/></svg>
    </li>
    <li>mcosgrove@BramblewickSys.com
      <svg viewBox="0 0 16 16" aria-hidden="true"><rect x="1" y="3" width="14" height="10" fill="var(--blue)"/><path d="M1.5 3.5L8 9l6.5-5.5" stroke="#fff" stroke-width="1.3" fill="none"/></svg>
    </li>
    <li>www.BramblewickSys.com
      <svg viewBox="0 0 16 16" aria-hidden="true"><circle cx="8" cy="8" r="7" fill="var(--blue)"/><path d="M1 8h14M8 1c-3 3-3 11 0 14M8 1c3 3 3 11 0 14" stroke="#fff" stroke-width="1" fill="none"/></svg>
    </li>
  </ul>
</section>

<section class="card card--back" aria-label="Business card back">
  <div class="brand">
    <span class="brand__mark"></span>
    <span class="brand__name">Bramblewick<br>Systems Group</span>
  </div>

  <div class="card__base"></div>
  <svg class="card__art" width="615" height="352" viewBox="0 0 615 352">
    <rect x="41" y="163" width="79" height="53" fill="#1a6fbf" opacity=".85" role="img" aria-label="Small cluster of blue, orange and white pixel squares"/>
  </svg>

  <div class="services">
    <p class="services__row">IT Security
      <svg viewBox="0 0 14 14" aria-hidden="true"><circle cx="7" cy="7" r="6.5" fill="#fff"/><path d="M4 7.2l2 2 4-4.4" stroke="var(--dark)" stroke-width="1.6" fill="none"/></svg>
      Projects
      <svg viewBox="0 0 14 14" aria-hidden="true"><circle cx="7" cy="7" r="6.5" fill="#fff"/><path d="M4 7.2l2 2 4-4.4" stroke="var(--dark)" stroke-width="1.6" fill="none"/></svg>
      Budgeting
      <svg viewBox="0 0 14 14" aria-hidden="true"><circle cx="7" cy="7" r="6.5" fill="#fff"/><path d="M4 7.2l2 2 4-4.4" stroke="var(--dark)" stroke-width="1.6" fill="none"/></svg>
      Consulting</p>
    <p class="services__row">Infrastructure
      <svg viewBox="0 0 14 14" aria-hidden="true"><circle cx="7" cy="7" r="6.5" fill="#fff"/><path d="M4 7.2l2 2 4-4.4" stroke="var(--dark)" stroke-width="1.6" fill="none"/></svg>
      Cloud/Hybrid
      <svg viewBox="0 0 14 14" aria-hidden="true"><circle cx="7" cy="7" r="6.5" fill="#fff"/><path d="M4 7.2l2 2 4-4.4" stroke="var(--dark)" stroke-width="1.6" fill="none"/></svg>
      Backup/DR
      <svg viewBox="0 0 14 14" aria-hidden="true"><circle cx="7" cy="7" r="6.5" fill="#fff"/><path d="M4 7.2l2 2 4-4.4" stroke="var(--dark)" stroke-width="1.6" fill="none"/></svg>
      VoIP</p>
  </div>
</section>

</body>
</html>
```